Web Design for photo printing service

Hi
I am looking for a new web design theme for our almost ready website http://fotoblik.zrmq.net, it will soon be launched under the name: www.zuna.is. (ZUNA means: You Only Live Once)

This is a website focused on printing photo products like: photo books, Greeting cards, posters, etc.

The whole theme should be playful, fun, creative. The marketing will be is that Life is fun, keep your memories. remember the good time etc.

So what I am looking for is a simple, yet colorful theme, easy to use.

We will be running max 4- 6 product groups, all extra info should be on the button,
expect shopping chart and sign in should be on top.

Extra feature:
Once a year during christmas, the web will turn on christmas outfit, it transforms
to Christmas looking Web. So a X-mas version would be fun to see !

Target Market(s)

Young people 20-35, young families.

Industry/Entity Type

Printing

Requirements
Must have
• Fun looking colorful design, simple to use.
Should not have
• Dark heavy look

```html
<!DOCTYPE html>
<html lang="en">
<head>
<meta charset="utf-8">
<title>ZUNA – Photo Printing</title>
<link rel="stylesheet" href="https://fonts.googleapis.com/css2?family=Raleway:wght@300;400;600;700;800&display=swap">
<style>
  :root {
    --blue: #0fa1c5;
    --purple: #9a2590;
    --forest: #2f4944;
    --orange: #f39341;
    --sage: #80bba8;
    --stone: #8d8d8d;
    --slate: #393a50;
    --red: #cf131a;
    --red-bright: #ee1c24;
    --ink: #1f1f1f;
    --bar: #2c2c2c;
    --fb: #1f77b8;
    --tw: #03a9e7;
    --gp: #de4221;
    --dr: #ec1657;
    --white: #ffffff;
  }
  * { box-sizing: border-box; margin: 0; padding: 0; }
  html, body { width: 827px; height: 1200px; overflow: hidden; background: #fff; }
  body { position: relative; font-family: "Raleway", sans-serif; color: var(--white); }
  .abs { position: absolute; }

  /* header */
  .brand { left: 0; top: 0; width: 171px; height: 58px; background: #fff; display: flex; align-items: center; gap: 8px; padding-left: 16px; }
  .brand-dot { width: 22px; height: 22px; border-radius: 50%; background: var(--blue); }
  .brand-name { font-weight: 800; font-size: 28px; color: var(--purple); letter-spacing: 1px; }
  .searchbar { left: 171px; top: 5px; width: 656px; height: 50px; background: linear-gradient(#1b1b1b, #2b2b2b); }
  .search-field { left: 187px; top: 22px; font-size: 13px; color: #666; }
  .search-btn { left: 640px; top: 10px; width: 93px; height: 41px; background: linear-gradient(#d9161d, #a80e13); display: flex; align-items: center; justify-content: center; gap: 6px; font-weight: 700; font-size: 15px; }
  .cart-btn { left: 739px; top: 7px; width: 85px; height: 46px; background: linear-gradient(#f22128, #c8121a); display: flex; align-items: center; justify-content: center; gap: 4px; font-weight: 700; font-size: 15px; }

  .nav { left: 0; top: 60px; width: 827px; height: 40px; background: linear-gradient(#2e2e2e, #161616); }
  .nav-inner { left: 20px; top: 61px; width: 788px; height: 38px; border-left: 1px solid #555; border-right: 1px solid #555; }
  .nav a { position: absolute; top: 18px; font-size: 11.5px; font-weight: 600; color: #fff; text-decoration: none; }

  /* tiles */
  .tile { display: flex; flex-direction: column; align-items: center; justify-content: center; text-align: center; gap: 32px; }
  .tile h2 { font-size: 14px; font-weight: 800; letter-spacing: .2px; line-height: 1.15; }
  .explore { width: 122px; height: 40px; border: 1px solid rgba(255,255,255,.9); display: flex; align-items: center; justify-content: center; font-size: 14px; font-weight: 400; letter-spacing: .3px; }
  .photo { }

  /* featured */
  .featured-label { left: 0; top: 575px; width: 297px; height: 65px; background: var(--red); display: flex; align-items: center; justify-content: center; font-weight: 800; font-size: 14px; }
  .featured-desc { left: 297px; top: 575px; width: 530px; height: 65px; background: linear-gradient(#333, #444); display: flex; align-items: center; justify-content: center; font-weight: 700; font-size: 14px; }
  .featured-rule { left: 307px; top: 581px; width: 4px; height: 52px; background: #fff; }
  .carousel { left: 0; top: 640px; width: 827px; height: 275px; background: radial-gradient(ellipse at 50% 40%, #6d6d6d, #474747); }
  .product { top: 701px; width: 165px; height: 110px; background: linear-gradient(135deg, #e7e2dc, #c86b39 40%, #7a1d18 60%, #d8d3cd); border: 1px solid #ddd; }
  .dots { left: 369px; top: 880px; display: flex; gap: 9px; }
  .dots span { width: 8px; height: 8px; border-radius: 50%; background: #fff; }
  .dots span.off { background: #aaa; }

  /* category strip */
  .cat { top: 915px; height: 120px; display: flex; align-items: center; justify-content: center; text-align: center; font-weight: 800; font-size: 14px; line-height: 1.15; }

  /* social */
  .social { top: 1035px; height: 100px; }
  .social-key { top: 1056px; width: 57px; height: 57px; border-radius: 4px; background: rgba(0,0,0,.25); box-shadow: 0 2px 3px rgba(0,0,0,.3); }

  /* footer */
  .footer { left: 0; top: 1135px; width: 827px; height: 65px; background: linear-gradient(#3a3a3a, #222); }
  .footer-text { left: 76px; top: 1160px; font-weight: 700; font-size: 14px; }
  .contact-btn { left: 550px; top: 1137px; width: 275px; height: 60px; background: linear-gradient(#f0161e, #c10f15); display: flex; align-items: center; justify-content: center; font-weight: 800; font-size: 14px; }
</style>
</head>
<body>

<header>
  <div class="abs brand"><span class="brand-dot"></span><span class="brand-name">ZUNA</span></div>
  <div class="abs searchbar"></div>
  <div class="abs search-field">search something here</div>
  <div class="abs search-btn">
    <svg width="18" height="18" viewBox="0 0 18 18"><circle cx="7" cy="7" r="5" fill="none" stroke="#fff" stroke-width="2"/><line x1="11" y1="11" x2="16" y2="16" stroke="#fff" stroke-width="2.5"/></svg>
    search
  </div>
  <div class="abs cart-btn">
    CART
    <svg width="26" height="22" viewBox="0 0 26 22"><path d="M1 2h4l3 12h14l3-9H7" fill="none" stroke="#fff" stroke-width="1.8"/><circle cx="10" cy="18" r="2" fill="#fff"/><circle cx="20" cy="18" r="2" fill="#fff"/></svg>
  </div>
</header>

<nav class="abs nav">
  <a style="left:40px">Photo Books</a>
  <a style="left:134px">Calendars</a>
  <a style="left:215px">Posters</a>
  <a style="left:281px">Opportunities Map</a>
  <a style="left:406px">Printed Photographs</a>
  <a style="left:546px">Our Price</a>
</nav>
<div class="abs nav-inner"></div>

<main>
  <div class="abs photo" style="left:0;top:101px;width:244px;height:158px;background:linear-gradient(135deg,#f4f4f4,#c9c3bd 50%,#f7f7f7)" role="img" aria-label="Open photo book with family pictures"></div>
  <div class="abs tile" style="left:244px;top:101px;width:174px;height:158px;background:var(--blue)"><h2>PHOTO BOOKS</h2><div class="explore">EXPLORE</div></div>
  <div class="abs photo" style="left:418px;top:101px;width:170px;height:158px;background:linear-gradient(#fff 8%,#5a4330 20%,#8a6a3e 45%,#e6ecb0 60%,#fff 95%)" role="img" aria-label="Spiral wall calendar with forest photo"></div>
  <div class="abs tile" style="left:588px;top:101px;width:239px;height:158px;background:var(--purple)"><h2>CALENDARS</h2><div class="explore">EXPLORE</div></div>

  <div class="abs tile" style="left:0;top:259px;width:244px;height:159px;background:var(--forest)"><h2>POSTERS</h2><div class="explore">EXPLORE</div></div>
  <div class="abs photo" style="left:244px;top:259px;width:174px;height:159px;background:radial-gradient(ellipse,#8a7b6c 30%,#d9d4ce 60%,#fff 75%)" role="img" aria-label="Collage poster of many small photos"></div>
  <div class="abs tile" style="left:418px;top:259px;width:170px;height:159px;background:var(--orange)"><h2>OPPORTUNITIES<br>MAP</h2><div class="explore">EXPLORE</div></div>
  <div class="abs photo" style="left:588px;top:259px;width:239px;height:159px;background:radial-gradient(ellipse at 55% 45%,#c99a55,#8a5b2b 40%,#eee 70%,#fff)" role="img" aria-label="New Year greeting card"></div>

  <div class="abs photo" style="left:0;top:418px;width:244px;height:157px;background:radial-gradient(ellipse,#6f8aa3,#b89a7a 45%,#fff 75%)" role="img" aria-label="Scattered printed holiday photographs"></div>
  <div class="abs tile" style="left:244px;top:418px;width:174px;height:157px;background:var(--sage)"><h2>PRINTED<br>PHOTOGRAPHS</h2><div class="explore">EXPLORE</div></div>
  <div class="abs" style="left:418px;top:418px;width:170px;height:157px;background:var(--stone)"></div>
  <div class="abs tile" style="left:588px;top:418px;width:239px;height:157px;background:var(--slate)"><h2>MORE</h2><div class="explore">EXPLORE</div></div>
</main>

<section>
  <div class="abs featured-label">FEATURED PRODUCTS</div>
  <div class="abs featured-desc">PRODUCT DESCRIPTION GOES HERE</div>
  <div class="abs featured-rule"></div>
  <div class="abs carousel"></div>
  <div class="abs product" style="left:33px" role="img" aria-label="Featured product photo of assorted sweets"></div>
  <div class="abs product" style="left:234px" role="img" aria-label="Featured product photo of assorted sweets"></div>
  <div class="abs product" style="left:429px" role="img" aria-label="Featured product photo of assorted sweets"></div>
  <div class="abs product" style="left:625px" role="img" aria-label="Featured product photo of assorted sweets"></div>
  <div class="abs dots"><span></span><span></span><span></span><span class="off"></span><span></span></div>
</section>

<section>
  <div class="abs cat" style="left:0;width:138px;background:var(--blue)">PHOTO BOOKS</div>
  <div class="abs cat" style="left:138px;width:138px;background:var(--purple)">CALENDARS</div>
  <div class="abs cat" style="left:276px;width:138px;background:var(--forest)">POSTERS</div>
  <div class="abs cat" style="left:414px;width:138px;background:var(--orange)">OPPORTUNITIES<br>MAP</div>
  <div class="abs cat" style="left:552px;width:138px;background:var(--sage)">PRINTED<br>PHOTOGRAPHS</div>
  <div class="abs cat" style="left:690px;width:137px;background:var(--slate)">MORE</div>
  <svg class="abs" style="left:590px;top:915px" width="60" height="30" viewBox="0 0 60 30"><polygon points="0,0 60,0 30,30" fill="#000"/></svg>
</section>

<section>
  <div class="abs social" style="left:0;width:209px;background:var(--fb)"></div>
  <div class="abs social" style="left:209px;width:209px;background:var(--tw)"></div>
  <div class="abs social" style="left:418px;width:209px;background:var(--gp)"></div>
  <div class="abs social" style="left:627px;width:200px;background:var(--dr)"></div>
  <div class="abs social-key" style="left:133px"></div>
  <div class="abs social-key" style="left:347px"></div>
  <div class="abs social-key" style="left:542px"></div>
  <div class="abs social-key" style="left:752px"></div>
</section>

<footer>
  <div class="abs footer"></div>
  <div class="abs footer-text">Footer Here</div>
  <div class="abs contact-btn">QUICK CONTACT</div>
</footer>

</body>
</html>
```